Psychology practice - information brochure/flyer - half A4 page folded (4 sides)

We need a brochure/flyer to market our psychology service to GPs (Doctors). We need to demonstrate to the doctors that we are the right choice for their patients, and that we cover a large range of services so all of their patients needs are met. We will demonstrate this by listing our range of services and our team of psychologists. We have two locations in Sydney and offer high end services. I've attached our company logo but we remain flexible regarding the style of the brochures. I will provide more details (services, locations & psychologist credentials) once our preferred brochure design has been selected.

```html
<!DOCTYPE html>
<html lang="en">
<head>
<meta charset="utf-8">
<title>Clear Harbour Clinical Psychology – Brochure Cover</title>
<link rel="stylesheet" href="https://fonts.googleapis.com/css2?family=Montserrat:wght@400;500;700&display=swap">
<style>
  :root {
    --gold: #d9a52a;
    --gold-deep: #c8921d;
    --gold-light: #e6b938;
    --ink: #4a4a4a;
    --paper: #ffffff;
    --ring: #c9c9c9;
    --backdrop: #e9e7e3;
    --photo-a: #d8d2c8;
    --photo-b: #8a7f74;
  }
  * { box-sizing: border-box; margin: 0; padding: 0; }
  html, body { width: 1200px; height: 789px; overflow: hidden; }
  body {
    background: var(--backdrop);
    font-family: "Montserrat", sans-serif;
    position: relative;
  }
  .spread {
    position: absolute;
    left: 60px; top: 12px;
    width: 1080px; height: 765px;
    display: flex;
    box-shadow: 0 6px 24px rgba(0,0,0,.18);
  }
  .page { position: relative; width: 540px; height: 765px; overflow: hidden; }

  /* Back cover */
  .back-cover {
    background: linear-gradient(160deg, var(--gold-light) 0%, var(--gold) 55%, var(--gold-deep) 100%);
    color: var(--paper);
  }
  .brand-name {
    position: absolute; left: 70px; top: 300px;
    font-weight: 400; font-size: 34px; line-height: 1.05; letter-spacing: .5px;
  }
  .opening-note {
    position: absolute; left: 70px; top: 405px;
    font-weight: 700; font-size: 17px; line-height: 1.45; letter-spacing: .6px;
  }
  .opening-note .street { display: block; padding-left: 48px; font-weight: 500; }
  .contact-heading {
    position: absolute; left: 40px; right: 40px; top: 548px;
    text-align: center; font-weight: 500; font-size: 15px; line-height: 1.35; letter-spacing: .6px;
  }
  .contact-box {
    position: absolute; left: 40px; right: 40px; top: 575px; height: 150px;
    border: 1px solid rgba(255,255,255,.85);
    padding: 40px 22px 16px;
    font-size: 11px; line-height: 1.6;
    display: grid; grid-template-columns: 1.35fr 1fr; column-gap: 14px; row-gap: 10px;
  }
  .contact-heading span { background: var(--gold); padding: 0 10px; }
  .contact-item { display: flex; gap: 7px; align-items: flex-start; }
  .contact-item svg { flex: none; width: 11px; height: 11px; margin-top: 3px; fill: var(--paper); }
  .phones { font-size: 15px; font-weight: 500; line-height: 1.4; }

  /* Front cover */
  .front-cover { background: var(--paper); }
  .photo-ring {
    position: absolute; left: -90px; top: 70px;
    width: 460px; height: 460px; border-radius: 50%;
    border: 1.5px solid var(--ring);
  }
  .photo {
    position: absolute; left: -75px; top: 85px;
    width: 430px; height: 430px; border-radius: 50%;
    background: radial-gradient(circle at 60% 40%, var(--photo-a) 0%, #b8aea2 50%, var(--photo-b) 100%);
  }
  .badge {
    position: absolute; left: 305px; top: 38px;
    width: 190px; height: 190px; border-radius: 50%;
    background: var(--gold);
    display: flex; align-items: center; justify-content: center; text-align: center;
    color: var(--paper); font-weight: 400; font-size: 21px; line-height: 1.1;
  }
  .tagline {
    position: absolute; right: 40px; top: 500px;
    text-align: right; font-size: 27px; line-height: 1.08; letter-spacing: .5px;
    color: var(--ink); font-weight: 400;
  }
  .tagline .accent { color: var(--gold); font-weight: 700; display: block; }
  .footer-band { position: absolute; left: 0; bottom: 0; width: 540px; height: 130px; }
  .web-address {
    position: absolute; left: 0; right: 30px; bottom: 38px;
    text-align: right; color: var(--paper); font-size: 14px; letter-spacing: .5px;
  }
</style>
</head>
<body>
  <main class="spread">
    <section class="page back-cover">
      <div class="brand-name">Clear Harbour<br>Clinical Psychology</div>
      <p class="opening-note">NEW LOCATION OPENING SOON<span class="street">in Willow St Ashbury</span></p>
      <div class="contact-box">
        <div class="contact-item">
          <svg viewBox="0 0 12 12" aria-hidden="true"><path d="M6 0a4 4 0 0 0-4 4c0 3 4 8 4 8s4-5 4-8a4 4 0 0 0-4-4zm0 5.6A1.6 1.6 0 1 1 6 2.4a1.6 1.6 0 0 1 0 3.2z"/></svg>
          <span>Suite 4, Level 2, 18 Marlow Street, Kingsgrove 2208<br>Shop 7, 52 Willow St, Ashbury 2193</span>
        </div>
        <div class="phones">
          <div class="contact-item"><svg viewBox="0 0 12 12" aria-hidden="true"><path d="M2.5 0.5l2 2-1 1.5a7 7 0 0 0 4.5 4.5l1.5-1 2 2-1.5 2C5 11.5.5 7 .5 2z"/></svg><span>02 9000 1472</span></div>
          <div class="contact-item"><svg viewBox="0 0 12 12" aria-hidden="true"><path d="M3 1h6v3H3zM1 5h10v5H9v2H3v-2H1zM4 8v3h4V8z"/></svg><span>02 9000 1473</span></div>
        </div>
        <div class="contact-item">
          <svg viewBox="0 0 12 12" aria-hidden="true"><path d="M0 2h12v8H0zm1 1l5 4 5-4z"/></svg>
          <span>hello@clearharbourpsych.com.au</span>
        </div>
        <div class="contact-item">
          <svg viewBox="0 0 12 12" aria-hidden="true"><circle cx="6" cy="6" r="5.5"/></svg>
          <span>www.clearharbourpsych.com.au</span>
        </div>
      </div>
      <p class="contact-heading"><span>TO MAKE APPOINTMENTS PLEASE<br>CONTACT US ON BELOW</span></p>
    </section>

    <section class="page front-cover">
      <div class="photo-ring"></div>
      <div class="photo" role="img" aria-label="Photo of a psychologist shaking hands with a smiling couple seated on a sofa in a bright consulting room"></div>
      <div class="badge">Clear Harbour<br>Clinical Psychology</div>
      <h1 class="tagline">WORKING<br>TOGETHER<br>TO ACHIEVE<span class="accent">A BETTER<br>QUALITY OF LIFE</span></h1>
      <svg class="footer-band" viewBox="0 0 540 130" preserveAspectRatio="none" aria-hidden="true">
        <path d="M0 95 Q 270 60 540 20 L540 130 L0 130 Z" fill="var(--gold)"/>
      </svg>
      <p class="web-address">WWW.CLEARHARBOURPSYCH.COM.AU</p>
    </section>
  </main>
</body>
</html>
```